" Recebemos através de emails e mensagem solicitação de orçamento.Apos isso marcamos uma visita com o cliente para elaboração do orçamento depois enviamos a proposta em PDF com os trabalhos a serem executados "

```html
<!DOCTYPE html>
<html lang="pt-BR">
<head>
<meta charset="UTF-8">
<title>Vetor Eletro Engenharia — Papel Timbrado</title>
<link rel="stylesheet" href="https://fonts.googleapis.com/css2?family=Montserrat:wght@600&family=Open+Sans:wght@400;600&display=swap">
<style>
  :root {
    --brand-green: #1d4a3c;
    --paper: #ffffff;
    --backdrop: #e9e7e3;
    --mark-grey: #e3e5e4;
    --text-dark: #2b2b2b;
  }
  * { margin: 0; padding: 0; box-sizing: border-box; }
  html, body {
    width: 1200px; height: 1200px; overflow: hidden;
    background: var(--backdrop);
  }
  .letterhead {
    position: absolute; left: 211px; top: 50px;
    width: 778px; height: 1100px;
    background: var(--paper);
    box-shadow: 0 6px 24px rgba(0,0,0,.18);
    overflow: hidden;
  }
  .edge-tab {
    position: absolute; top: 25px; width: 15px; height: 65px;
    background: var(--brand-green);
  }
  .edge-tab--left { left: 0; }
  .edge-tab--right { right: 0; }

  .brand {
    position: absolute; top: 40px; left: 50%; transform: translateX(-50%);
    display: flex; align-items: center; gap: 12px;
    color: var(--brand-green);
    font-family: "Montserrat", sans-serif; font-weight: 600;
  }
  .brand__dot {
    width: 42px; height: 42px; border-radius: 50%;
    border: 4px solid var(--brand-green);
  }
  .brand__name { display: flex; flex-direction: column; line-height: 1; }
  .brand__title { font-size: 32px; letter-spacing: 2px; }
  .brand__tagline { font-size: 9.5px; letter-spacing: 2.2px; margin-top: 5px; }

  .watermark {
    position: absolute; left: 130px; top: 290px;
    width: 530px; height: 530px;
  }

  .contact-bar {
    position: absolute; left: 55px; right: 55px; top: 1040px;
    display: flex; align-items: center; justify-content: space-between;
    font-family: "Open Sans", sans-serif; font-size: 10px;
    color: var(--text-dark);
  }
  .contact-item { display: flex; align-items: center; gap: 7px; }
  .contact-item svg { width: 14px; height: 14px; flex: none; }
  .contact-item__lines { line-height: 1.35; }
  .social-square {
    width: 13px; height: 13px; border: 1.6px solid var(--text-dark); border-radius: 3px;
  }
  .footer-band {
    position: absolute; left: 0; right: 0; bottom: 12px; height: 15px;
    background: var(--brand-green);
  }
</style>
</head>
<body>
  <main class="letterhead">
    <div class="edge-tab edge-tab--left"></div>
    <div class="edge-tab edge-tab--right"></div>

    <header class="brand">
      <span class="brand__dot"></span>
      <span class="brand__name">
        <span class="brand__title">VETOR</span>
        <span class="brand__tagline">ELETRO ENGENHARIA</span>
      </span>
    </header>

    <svg class="watermark" viewBox="0 0 530 530" aria-hidden="true">
      <circle cx="265" cy="265" r="240" fill="none" stroke="var(--mark-grey)" stroke-width="34"/>
    </svg>

    <footer class="contact-bar">
      <div class="contact-item">
        <svg viewBox="0 0 24 24"><path d="M6.6 10.8a15.1 15.1 0 0 0 6.6 6.6l2.2-2.2a1 1 0 0 1 1-.25 11.4 11.4 0 0 0 3.6.57 1 1 0 0 1 1 1V20a1 1 0 0 1-1 1A17 17 0 0 1 3 4a1 1 0 0 1 1-1h3.5a1 1 0 0 1 1 1c0 1.25.2 2.45.57 3.57a1 1 0 0 1-.25 1z" fill="var(--text-dark)"/></svg>
        <span>00 0000-0000 | 00 00000-0000</span>
      </div>
      <div class="contact-item">
        <svg viewBox="0 0 24 24"><rect x="2.5" y="5" width="19" height="14" rx="1.5" fill="none" stroke="var(--text-dark)" stroke-width="2"/><path d="M3 6l9 7 9-7" fill="none" stroke="var(--text-dark)" stroke-width="2"/></svg>
        <span>contato@vetoreletro.com.br</span>
      </div>
      <div class="contact-item">
        <svg viewBox="0 0 24 24"><path d="M12 2a7 7 0 0 0-7 7c0 5.25 7 13 7 13s7-7.75 7-13a7 7 0 0 0-7-7zm0 9.5A2.5 2.5 0 1 1 12 6.5a2.5 2.5 0 0 1 0 5z" fill="var(--text-dark)"/></svg>
        <span class="contact-item__lines">Nome da Rua, 00 - Bairro<br>Cidade - Estado e CEP</span>
      </div>
      <div class="contact-item">
        <span class="social-square"></span>
        <span>vetoreletro</span>
      </div>
    </footer>

    <div class="footer-band"></div>
  </main>
</body>
</html>
```